New Zealand Luggage Importer Needs Business Cards

We need professional, creative and fashionable business cards created.
We are based in New Zealand and import and distribute high-end, quality, fashionable and durable luggage.
We pride ourselves on selling the very best quality luggage, second only to 1 brand (which we won't mention here)...we use the same manufacturer. However, our prices are much more reasonable.
Industry/Entity Type
Business
Contact Information for Business Card
Mark Dunsley
027 512 4068
3/17 Harlow Street, Pinecrest Flats, Auckland, 0614
PO Box 204377, Fernside, Auckland 0731
09-528-3916
sales@brivancases.co.nz / www.brivancases.co.nz

```html
<!DOCTYPE html>
<html lang="en">
<head>
<meta charset="utf-8">
<title>Brivan Cases – Business Card</title>
<link href="https://fonts.googleapis.com/css2?family=Lato:wght@400;700;900&display=swap" rel="stylesheet">
<style>
  :root {
    --ink: #121212;
    --white: #ffffff;
    --gold-deep: #cf9c2e;
    --gold-mid: #d9b247;
    --gold-light: #ecdb7a;
    --page: #ffffff;
  }
  html, body { margin: 0; padding: 0; overflow: hidden; }
  body {
    width: 1200px; height: 1000px;
    background: var(--page);
    position: relative;
    font-family: "Lato", Arial, sans-serif;
  }
  .card { position: absolute; left: 355px; width: 536px; }
  .card-front { top: 145px; height: 305px; }
  .card-back { top: 488px; height: 304px; }
  .card svg.card-shape { position: absolute; inset: 0; width: 100%; height: 100%; }

  .brand-name {
    position: absolute; left: 0; right: 0;
    text-align: center;
    color: var(--white);
    font-weight: 900;
    font-size: 36px;
    letter-spacing: 5px;
    line-height: 1;
  }
  .card-front .brand-name { top: 134px; }
  .card-back .brand-name { top: 66px; }

  .front-url {
    position: absolute; left: 0; right: 0; top: 250px;
    text-align: center; color: var(--white);
    font-weight: 700; font-size: 14px; letter-spacing: 1px;
  }

  .holder {
    position: absolute; right: 327px; top: 178px; text-align: right;
  }
  .holder-name {
    font-weight: 900; font-size: 20px; letter-spacing: 3px;
    color: var(--ink); line-height: 1;
  }
  .holder-title {
    font-size: 13px; letter-spacing: 0.6px; color: var(--ink); margin-top: 7px;
  }

  .contacts {
    position: absolute; left: 316px; top: 161px;
    list-style: none; margin: 0; padding: 0;
  }
  .contacts li {
    display: flex; align-items: center; gap: 7px;
    font-size: 13px; letter-spacing: 0.6px; color: var(--ink);
    height: 20.5px;
  }
  .contacts svg { width: 10px; height: 10px; flex: none; }

  .address {
    position: absolute; left: 0; right: 0; top: 261px;
    text-align: center; color: var(--white);
    font-size: 12.5px; line-height: 17px;
  }
</style>
</head>
<body>

<section class="card card-front">
  <svg class="card-shape" viewBox="0 0 536 305" aria-hidden="true">
    <defs>
      <linearGradient id="frontGold" x1="0" y1="0" x2="1" y2="0.3">
        <stop offset="0" stop-color="var(--gold-deep)"/>
        <stop offset="0.5" stop-color="var(--gold-mid)"/>
        <stop offset="1" stop-color="var(--gold-light)"/>
      </linearGradient>
    </defs>
    <rect width="536" height="305" rx="24" fill="url(#frontGold)"/>
    <path d="M24 0 H512 A24 24 0 0 1 536 24 V250 A35 35 0 0 1 501 285 H35 A35 35 0 0 1 0 250 V24 A24 24 0 0 1 24 0 Z" fill="var(--ink)"/>
  </svg>
  <div class="brand-name">BRIVAN CASES</div>
  <div class="front-url">www.brivancases.co.nz</div>
</section>

<section class="card card-back">
  <svg class="card-shape" viewBox="0 0 536 304" aria-hidden="true">
    <defs>
      <linearGradient id="backGold" x1="0" y1="0" x2="0" y2="1">
        <stop offset="0.3" stop-color="var(--gold-mid)"/>
        <stop offset="0.8" stop-color="var(--gold-light)"/>
      </linearGradient>
      <clipPath id="backClip"><rect width="536" height="304" rx="24"/></clipPath>
    </defs>
    <g clip-path="url(#backClip)">
      <rect width="536" height="304" fill="url(#backGold)"/>
      <rect width="536" height="110" fill="var(--ink)"/>
      <rect x="10" y="0" width="516" height="144" rx="22" fill="var(--ink)"/>
      <path d="M0 100 V134 Q7 120 10 100 Z" fill="var(--ink)"/>
      <path d="M536 100 V134 Q529 120 526 100 Z" fill="var(--ink)"/>
      <rect y="255" width="536" height="49" fill="var(--ink)"/>
      <polygon points="268,166 269.2,202 268,238 266.8,202" fill="var(--ink)"/>
    </g>
  </svg>

  <div class="brand-name">BRIVAN CASES</div>

  <div class="holder">
    <div class="holder-name">MARK DUNSLEY</div>
    <div class="holder-title">President</div>
  </div>

  <ul class="contacts">
    <li>
      <svg viewBox="0 0 10 10"><rect width="10" height="10" rx="2" fill="var(--ink)"/><path d="M3 2.3 L4.2 3.6 L3.6 4.3 Q4.6 5.8 5.8 6.4 L6.5 5.8 L7.7 7 L6.9 7.9 Q3.9 7.3 2.2 3.2 Z" fill="var(--gold-light)"/></svg>
      027 512 4068
    </li>
    <li>
      <svg viewBox="0 0 10 10"><rect width="10" height="10" rx="2" fill="var(--ink)"/><path d="M3 2.3 L4.2 3.6 L3.6 4.3 Q4.6 5.8 5.8 6.4 L6.5 5.8 L7.7 7 L6.9 7.9 Q3.9 7.3 2.2 3.2 Z" fill="var(--gold-light)"/></svg>
      09 528 3916
    </li>
    <li>
      <svg viewBox="0 0 10 10"><rect width="10" height="10" rx="2" fill="var(--ink)"/><path d="M2.2 5 L7.8 2.4 L5.6 7.8 L4.8 5.4 Z" fill="var(--gold-light)"/></svg>
      sales@brivancases.co.nz
    </li>
    <li>
      <svg viewBox="0 0 10 10"><rect width="10" height="10" rx="2" fill="var(--ink)"/><path d="M3 7 L7 3 M2.6 5.4 L4.6 7.4 M5.4 2.6 L7.4 4.6" stroke="var(--gold-light)" stroke-width="1.2" fill="none"/></svg>
      www.brivancases.co.nz
    </li>
  </ul>

  <div class="address">3/17 Harlow Street, Pinecrest Flats, Auckland, 0614, PO Box 204377,<br>Fernside, Auckland 0731</div>
</section>

</body>
</html>
```